Concierge Healthcare Business Card Design and Logo

We need a logo and business card design for a new company called "Sound Harbor". We will provide concierge audiological care, hearing aids, hearing exams, custom hearing protection etc to patients in the comfort of their homes and offices. We would like a sleek and modern design preferably with an Ear related logo.

Target Market(s)

People with hearing loss, Hunters, Musicians
My usual clientele are older individuals so usually 50+ years old

Industry/Entity Type

Health Care

Contact Information for Business Card

Delia Franks, AuD
Audiologist
512-648-2917
soundharbor@mailnest.com
www.soundharbor-example.com

Logo Text

Sound Harbor

Number of Pages Required

3 page

```html
<!DOCTYPE html>
<html lang="en">
<head>
<meta charset="utf-8">
<title>Sound Harbor – Business Card</title>
<link rel="stylesheet" href="https://fonts.googleapis.com/css2?family=Open+Sans:wght@400;600;700&family=Questrial&display=swap">
<style>
  :root {
    --page-bg: #e9e7e6;
    --card-top: #f6f4f3;
    --brand-blue: #0b93dc;
    --ink: #1b1b1b;
    --on-blue: #ffffff;
    --ghost: rgba(60, 70, 80, 0.22);
  }
  * { margin: 0; padding: 0; box-sizing: border-box; }
  html, body { width: 1200px; height: 900px; overflow: hidden; }
  body {
    background: var(--page-bg);
    position: relative;
    font-family: "Open Sans", Arial, sans-serif;
  }
  .card {
    position: absolute;
    background: var(--card-top);
    overflow: hidden;
    box-shadow: 0 6px 18px rgba(0,0,0,0.12);
  }
  .card--front { left: 238px; top: 62px; width: 555px; height: 342px; }
  .card--back  { left: 457px; top: 518px; width: 560px; height: 344px; }
  .card__band {
    position: absolute; left: 0; right: 0; bottom: 0;
    background: var(--brand-blue);
    color: var(--on-blue);
  }
  .card--front .card__band { height: 156px; }
  .card--back .card__band { height: 157px; }

  .brand {
    position: absolute;
    display: flex; align-items: center; gap: 14px;
    font-family: "Questrial", "Century Gothic", sans-serif;
    font-size: 46px; line-height: 1;
    color: var(--ink);
  }
  .card--front .brand { left: 110px; top: 82px; }
  .brand__dot {
    width: 34px; height: 34px; border-radius: 50%;
    background: var(--brand-blue);
  }
  .brand--ghost {
    color: var(--ghost);
    transform: scaleX(-1);
    left: 114px; top: 82px;
  }
  .brand--ghost .brand__dot { background: rgba(11,147,220,0.3); }

  .person {
    position: absolute; right: 291px; top: 219px;
    text-align: right;
  }
  .person__name { font-size: 19px; font-weight: 700; line-height: 24px; }
  .person__role { font-size: 14px; line-height: 20px; margin-top: 0; }

  .contact {
    position: absolute; left: 286px; top: 209px;
    list-style: none;
    font-size: 14.5px; line-height: 20px;
  }
  .contact__item { display: flex; align-items: center; gap: 9px; }
  .contact__icon { width: 12px; height: 12px; fill: var(--on-blue); flex: none; }

  .address {
    position: absolute; left: 104px; top: 288px;
    font-size: 14.5px; line-height: 20px;
  }
  .back-web {
    position: absolute; left: 0; right: 0; bottom: 27px;
    text-align: center; font-size: 14.5px;
  }
</style>
</head>
<body>
  <section class="card card--front" aria-label="Business card front">
    <div class="brand"><span class="brand__name">Sound Harbor</span><span class="brand__dot"></span></div>
    <div class="card__band"></div>
    <div class="person" style="color: var(--on-blue)">
      <p class="person__name">Delia Franks</p>
      <p class="person__role">Managing Director</p>
    </div>
    <ul class="contact" style="color: var(--on-blue)">
      <li class="contact__item">
        <svg class="contact__icon" viewBox="0 0 24 24"><path d="M6.6 10.8a15.1 15.1 0 0 0 6.6 6.6l2.2-2.2a1 1 0 0 1 1-.25 11.4 11.4 0 0 0 3.6.57 1 1 0 0 1 1 1V20a1 1 0 0 1-1 1A17 17 0 0 1 3 4a1 1 0 0 1 1-1h3.5a1 1 0 0 1 1 1c0 1.25.2 2.45.57 3.57a1 1 0 0 1-.25 1z"/></svg>
        <span>512-648-2917</span>
      </li>
      <li class="contact__item">
        <svg class="contact__icon" viewBox="0 0 24 24"><path d="M2 6h20v12H2z" fill="none" stroke="#fff" stroke-width="2.5"/><path d="M2 6l10 7 10-7" fill="none" stroke="#fff" stroke-width="2.5"/></svg>
        <span>soundharbor@mailnest.com</span>
      </li>
      <li class="contact__item">
        <svg class="contact__icon" viewBox="0 0 24 24"><circle cx="12" cy="12" r="10"/><path d="M5 9h6l1 4-3 2v4M14 4l1 4h4M15 20l1-4 3-1" fill="none" stroke="#0b93dc" stroke-width="1.8"/></svg>
        <span>www.soundharbor-example.com</span>
      </li>
    </ul>
    <p class="address" style="color: var(--on-blue)">4410 Harbor Lane, Austin, Texas, 78701.</p>
  </section>

  <section class="card card--back" aria-label="Business card back">
    <div class="brand brand--ghost" aria-hidden="true"><span class="brand__name">Sound Harbor</span><span class="brand__dot"></span></div>
    <div class="card__band">
      <p class="back-web">www.soundharbor-example.com</p>
    </div>
  </section>
</body>
</html>
```